Redesign of outdated "Automotive Automation Company"

We are looking to finally update our outdated website with some cutting edge graphics. We want our customers to know we value technology and are cutting edge as far as design. We provide automation solutions for the automotive industry which essentially means we program robots, and sell automation related products.

Current URL

http://lnk.vexor.test/Qm7trz
Updates

Project Deadline Extended
Reason: The client portal wasn't working, it's just finally been fixed by Pixel Harbor. I will go through and start reviewing designs.

We are trying to go with the same look and feel on our business cards, line cards, apparel, etc. so we are forming a brand. I have included the current draft of the line card. Please utilize our newest Logo TMV Standardized Logo.jpg http://img.pelvarhost.test/zq4Rb8d.jpg?1 Also we are trying hard to sell the following software / hardware companies so we can put some emphasis on their product. Corvane Systems https://www.corvanesystems.test/ We make money on selling the software and then on the integration. I think you should tie in this animation. ยท Shop Line Tangle to Throughput https://media.vidloft.test/deliveries/9b2e7c41d05f83a6c17e2d94b0a6f3e1c85d7b42.jpg?image_play_button=true&image_play_button_color=7b796ae0&image_crop_resized=275x155 In this 2-minute video, discover how Keystroke can help run your plant floor. We are Authorized Integrators / Resellers for Halbrook Controls Tavrin Sensorik http://tavrin.test/en/usa/ Corvane Systems https://www.corvanesystems.test/ Meridel Process Works www.mpwxx.test Solbry Belt Corp www.solbrybelt.test Quellmark Fabrication http://www.quellmarkfab.test/strategic_partners.aspx

Target Market(s)

Large automotive companies looking for automation or robotic programming. So Professional is key.

Industry/Entity Type

Automotive

Font styles to use
Other font styles liked:
• Possible Open Sans or Lato

Colors
0591cc
ceeaf6
fbd4d5
fbf289
fece3e

Requirements
Must have
• Professional Modern Design.

I want a homepage design, and a rough Sales Page... Where numerous products can be listed.
Nice to have
• Maybe an updated logo if possible.

```html
<!DOCTYPE html>
<html lang="en">
<head>
<meta charset="utf-8">
<title>TMV Engineering Solutions, INC</title>
<link rel="stylesheet" href="https://fonts.googleapis.com/css2?family=Lato:wght@300;400;700&family=Arimo:wght@400&display=swap">
<style>
:root{
  --brand-blue:#0591cc;
  --link-blue:#1a8fd0;
  --hero-top:#1c8cc6;
  --hero-bottom:#0f78b3;
  --ink:#444;
  --muted:#777;
  --rule:#dcdcdc;
  --panel:#f3f3f3;
  --accent-yellow:#fece3e;
  --footer:#545454;
  --footer-text:#c9c9c9;
  --white:#fff;
}
*{box-sizing:border-box;margin:0;padding:0}
html,body{width:1200px;height:1112px;overflow:hidden;background:var(--white)}
body{font-family:"Lato",sans-serif;color:var(--ink);position:relative}
.wrap{position:absolute;left:269px;width:649px}

/* header */
.site-header{position:absolute;top:0;left:0;width:1200px;height:62px;background:var(--white)}
.brand{position:absolute;left:269px;top:12px;display:flex;align-items:flex-start;gap:12px}
.brand-mark{width:40px;height:40px;background:var(--brand-blue);margin-top:1px}
.brand-name{font-family:"Arimo",sans-serif;font-size:16px;color:#222;line-height:20px}
.brand-tagline{font-family:"Arimo",sans-serif;font-size:9px;color:#555;letter-spacing:.6px;margin-top:5px}
.main-nav{position:absolute;top:27px;left:708px;display:flex;gap:0}
.main-nav a{font-size:10px;color:#666;text-decoration:none;font-family:"Lato",sans-serif}
.main-nav a:nth-child(1){position:absolute;left:0}
.main-nav a:nth-child(2){position:absolute;left:54px}
.main-nav a:nth-child(3){position:absolute;left:113px}
.main-nav a:nth-child(4){position:absolute;left:166px;white-space:nowrap}

/* hero */
.hero{position:absolute;top:62px;left:0;width:1200px;height:296px;
  background:radial-gradient(ellipse at 30% 60%,#2a9bd3 0%,transparent 55%),linear-gradient(180deg,var(--hero-top),var(--hero-bottom))}
.hero-text{position:absolute;top:102px;left:0;width:1200px;text-align:center;color:var(--white)}
.hero-phone{font-size:15px;margin-left:-9px}
.hero-sub{font-size:11px;margin-top:15px}
.hero-title{font-size:24px;font-weight:400;margin-top:5px}
.dots{position:absolute;top:268px;left:578px;display:flex;gap:3px}
.dots span{width:7px;height:7px;border-radius:50%;background:var(--white)}
.dots span:first-child{background:#1e1e1e}

/* feature bar */
.feature-bar{position:absolute;top:358px;left:0;width:1200px;height:37px;border-bottom:1px solid var(--rule)}
.feature{position:absolute;top:12px;display:flex;align-items:center;gap:12px;font-size:10px;color:#333}
.feature.is-active{color:var(--link-blue)}
.feature svg{width:18px;height:18px}
.sep{position:absolute;top:14px;width:1px;height:10px;background:#ccc}

/* profile */
.profile-title{top:420px;text-align:center;font-size:15px;color:#444;font-weight:400}
.profile-text{top:454px;text-align:center;font-size:7.5px;line-height:14px;color:#666}

/* products */
.products{top:520px;height:153px;background:linear-gradient(180deg,var(--panel) 60%,var(--white))}
.products-head{position:absolute;top:18px;left:16px;font-size:7.5px;color:#444;letter-spacing:.2px}
.list-all{position:absolute;top:19px;right:15px;font-size:6.5px;color:#666;text-decoration:underline}
.card{position:absolute;top:36px;width:198px;height:117px;border-top:3px solid var(--accent-yellow);background:linear-gradient(180deg,var(--white) 70%,#fafafa)}
.card-photo{position:absolute;top:10px;left:69px;width:60px;height:66px;background:linear-gradient(180deg,#6b6b6b,#2e2e2e);border-radius:4px}
.card-rule{position:absolute;top:88px;left:15px;right:12px;height:1px;background:var(--rule)}
.card-caption{position:absolute;top:97px;width:100%;text-align:center;font-size:7.5px;color:#777}

/* lower */
.consult-title{position:absolute;top:711px;left:301px;font-size:11.5px;line-height:18px;color:#444;width:200px}
.link-list{position:absolute;top:758px;left:300px;list-style:none}
.link-list li{font-size:7.8px;color:var(--link-blue);height:17.5px}
.videos-title{position:absolute;top:713px;left:547px;font-size:11.5px;color:#444}
.video{position:absolute;top:760px;width:182px;height:97px}
.video-1{left:547px;background:linear-gradient(90deg,#e9c7b9,#c98f7a 60%,#b07764)}
.video-2{left:736px;background:linear-gradient(135deg,#c9cdd2,#eef0f2 55%,#b6bcc3)}
.play{position:absolute;top:38px;left:80px;width:22px;height:22px}

/* distributors */
.distributors{position:absolute;top:941px;left:0;width:1200px;height:122px;background:var(--panel)}
.dist-title{position:absolute;top:26px;width:1200px;text-align:center;font-size:8.5px;color:#555;letter-spacing:.3px}
.dist-rule{position:absolute;top:46px;left:269px;width:649px;height:1px;background:var(--rule)}
.dist-sub{position:absolute;top:41px;left:0;width:1200px;text-align:center}
.dist-sub span{background:var(--panel);padding:0 10px;font-size:7.8px;color:#666}
.partner{position:absolute;top:78px;display:flex;align-items:center;gap:7px;font-size:16px;font-weight:700;color:#8a8a8a}
.partner i{display:block;width:14px;height:14px;background:#8a8a8a;border-radius:50%}

/* footer */
.site-footer{position:absolute;top:1063px;left:0;width:1200px;height:49px;background:var(--footer)}
.social{position:absolute;top:16px;left:270px;display:flex;gap:10px}
.social span{width:18px;height:18px;border-radius:50%;background:#8d8d8d}
.footer-contact{position:absolute;top:22px;left:366px;font-size:6.5px;color:var(--footer-text)}
.copyright{position:absolute;top:22px;right:282px;font-size:6.5px;color:var(--footer-text)}
</style>
</head>
<body>

<header class="site-header">
  <div class="brand">
    <div class="brand-mark"></div>
    <div>
      <div class="brand-name">TMV Engineering Solutions, INC</div>
      <div class="brand-tagline">AUTOMATION &nbsp;•&nbsp; ROBOTICS &nbsp;•&nbsp; CONTROLS</div>
    </div>
  </div>
  <nav class="main-nav">
    <a href="#">Home</a><a href="#">Services</a><a href="#">About Us</a><a href="#">Contact Us</a>
  </nav>
</header>

<section class="hero" role="img" aria-label="Blue background of interlocking gears with a hand turning one">
  <div class="hero-text">
    <div class="hero-phone">1-855-MOTION-GO</div>
    <div class="hero-sub">Your Premier Automation Consulting &amp; Systems Integration choice!</div>
    <h1 class="hero-title">Helping your business optimize its Automation....</h1>
  </div>
  <div class="dots"><span></span><span></span><span></span></div>
</section>

<div class="feature-bar">
  <div class="feature is-active" style="left:269px">
    <svg viewBox="0 0 18 18" fill="none" stroke="#1a8fd0" stroke-width="1.3"><circle cx="9" cy="9" r="7.5"/><path d="M9 4.5V9l3 2"/></svg>
    Get to know our Team approach
  </div>
  <div class="sep" style="left:452px"></div>
  <div class="feature" style="left:483px">
    <svg viewBox="0 0 18 18" fill="none" stroke="#555" stroke-width="1.3"><path d="M3 15l7-7M11 3l4 4-3 1-2-2zM3 3l4 4M15 15l-5-5"/></svg>
    This way to Automation success
  </div>
  <div class="sep" style="left:665px"></div>
  <div class="feature" style="left:703px">
    <svg viewBox="0 0 18 18" fill="none" stroke="#555" stroke-width="1.3"><circle cx="7" cy="10" r="4"/><circle cx="7" cy="10" r="1.3"/><circle cx="13" cy="6" r="2.6"/></svg>
    This way to Automation success
  </div>
</div>

<h2 class="wrap profile-title">Company Profile</h2>
<p class="wrap profile-text">Industrial Automation is constantly evolving with ever-changing technological breakthroughs. For companies to remain competitive, they need to be more nimble than ever implementing productivity and manufacturing innovations. But identifying and implementing the right Automation, Robotics and industrial Controls is never easy. That's where our team of experts comes in to play bringing our proven experience to the table.</p>

<section class="wrap products">
  <div class="products-head">PRODUCT CATEGORIES</div>
  <div class="list-all">+ LIST ALL</div>
  <div class="card" style="left:16px">
    <div class="card-photo" role="img" aria-label="Industrial barcode scanner"></div>
    <div class="card-rule"></div>
    <div class="card-caption">Codes simplify communication in automation</div>
  </div>
  <div class="card" style="left:225px">
    <div class="card-photo" role="img" aria-label="Compact photoelectric sensor" style="left:84px;width:30px"></div>
    <div class="card-rule"></div>
    <div class="card-caption">Codes simplify communication in automation</div>
  </div>
  <div class="card" style="left:436px">
    <div class="card-photo" role="img" aria-label="Industrial data module with connectors" style="left:62px;width:74px;height:44px;top:22px"></div>
    <div class="card-rule"></div>
    <div class="card-caption">Codes simplify communication in automation</div>
  </div>
</section>

<h3 class="consult-title" style="font-weight:400">Your Premier Automation Consulting &amp; Systems Integration choice!</h3>
<ul class="link-list">
  <li>Product innovations</li>
  <li>Videos</li>
  <li>Switching Sensors</li>
  <li>Measuring Sensors</li>
  <li>Products for safety at work</li>
  <li>Identification</li>
  <li>Data transmission/control components</li>
  <li>Industrial image processing</li>
  <li>Accessories</li>
</ul>

<h3 class="videos-title" style="font-weight:400">Recently Update Videos</h3>
<div class="video video-1" role="img" aria-label="Video thumbnail: close-up portrait">
  <svg class="play" viewBox="0 0 22 22"><circle cx="11" cy="11" r="11" fill="rgba(120,120,110,.85)"/><path d="M8.5 6.5l7 4.5-7 4.5z" fill="#fff"/></svg>
</div>
<div class="video video-2" role="img" aria-label="Video thumbnail: hands reviewing charts on a tablet">
  <svg class="play" viewBox="0 0 22 22"><circle cx="11" cy="11" r="11" fill="rgba(120,120,110,.85)"/><path d="M8.5 6.5l7 4.5-7 4.5z" fill="#fff"/></svg>
</div>

<section class="distributors">
  <div class="dist-title">AUTHORIZED DISTRIBUTOR</div>
  <div class="dist-rule"></div>
  <div class="dist-sub"><span>Representing the following category specific manufacturers</span></div>
  <div class="partner" style="left:334px"><i></i>Tavrin Sensorik</div>
  <div class="partner" style="left:528px">Halbrook Controls</div>
  <div class="partner" style="left:703px"><i></i>Corvane Systems</div>
</section>

<footer class="site-footer">
  <div class="social"><span></span><span></span><span></span></div>
  <div class="footer-contact">1•855•MOTION•GO www.tmvengsolutions.test • 402 W. Larkfield Ave • PO Box 318 • Orrin, MI 48120</div>
  <div class="copyright">Copyright 2015 Company Name</div>
</footer>

</body>
</html>
```